Brindle painting & waterproofing business card.

Business cards updated to reflect photos attached. we have given the photos of the old business cards and some of our updated designs for other items we have here in the office. Please see attached. if anyone needs to contact us directly for clarification you can email us at brindlerestoration@mailcove.example

Industry/Entity Type

Construction

Contact Information for Business Card

See attached photos

Font styles to use
Other font styles liked:
• Same as photos

Colors
ec1f27

Requirements
Must have
• Employee Names,
• Dennis Marlow II, Supervisor/Owner
• Dee Marlow, President/Owner
• Gus Tremby, Sales Representative
• Lyle Varsen, Supervisor
• Change 20 years to 25
Nice to have
• ideas reflecting the attached photos
Should not have
• should not be exactly like attached photos as those are old business card but reflect to match new logo listed as korvel van and cup photo.

```html
<!DOCTYPE html>
<html lang="en">
<head>
<meta charset="utf-8">
<title>Brindle's Painting & Restoration – Business Card</title>
<link rel="stylesheet" href="https://fonts.googleapis.com/css2?family=Poppins:wght@300;400;500;600;800&display=swap">
<style>
  :root {
    --bg: #7a7a7a;
    --card: #f7f7f7;
    --red: #ec1f27;
    --ink: #1c1c1c;
    --muted: #555;
    --faint: #e6e6e6;
  }
  * { box-sizing: border-box; margin: 0; padding: 0; }
  html, body { width: 1200px; height: 960px; overflow: hidden; }
  body {
    background: var(--bg);
    font-family: "Poppins", sans-serif;
    color: var(--ink);
    position: relative;
  }
  .card {
    position: absolute;
    width: 640px;
    height: 380px;
    background: var(--card);
    border-radius: 26px;
    box-shadow: 0 10px 26px rgba(0,0,0,.28);
    overflow: hidden;
  }
  .card--front { left: 60px; top: 80px; }
  .card--back  { left: 500px; top: 500px; }

  /* front */
  .anniversary {
    position: absolute; right: 36px; top: 26px;
    display: flex; align-items: center; gap: 4px;
    color: var(--red);
  }
  .anniversary__number { font-size: 46px; font-weight: 300; line-height: 1; }
  .anniversary__label { display: flex; flex-direction: column; line-height: 1.05; }
  .anniversary__small { font-size: 7px; letter-spacing: .5px; color: var(--muted); }
  .anniversary__word { font-size: 16px; font-weight: 400; color: var(--ink); }

  .front-body {
    position: absolute; left: 0; right: 0; top: 96px;
    text-align: center;
  }
  .brand-name {
    font-size: 34px; font-weight: 800; color: var(--red);
    line-height: 1.05; letter-spacing: .5px;
  }
  .brand-sub {
    font-size: 22px; font-weight: 800; color: var(--red);
    line-height: 1.1; margin-bottom: 12px;
  }
  .specialty {
    font-size: 13px; font-weight: 500; color: var(--red);
    text-transform: uppercase; line-height: 1.35;
  }
  .credentials {
    font-size: 10px; color: var(--muted); margin: 6px 0 14px;
  }
  .services {
    font-size: 15px; font-weight: 400; line-height: 1.45;
  }
  .services .dot { color: var(--red); margin: 0 6px; }

  /* back */
  .person {
    position: absolute; right: 34px; top: 30px; text-align: right;
  }
  .person__name { font-size: 24px; font-weight: 500; color: var(--red); line-height: 1.2; }
  .person__role { font-size: 14px; font-weight: 500; }
  .person__web { font-size: 14px; }

  .brand-faint {
    position: absolute; left: 0; right: 0; top: 138px;
    text-align: center; color: var(--faint);
    font-size: 44px; font-weight: 800; line-height: 1.05;
  }
  .contact {
    position: absolute; left: 34px; bottom: 28px;
    font-size: 15px; line-height: 1.4;
  }
  .contact__address { margin-bottom: 4px; }
  .contact__row { display: flex; align-items: center; gap: 10px; }
  .contact__row svg { width: 15px; height: 15px; flex: none; }
</style>
</head>
<body>

<section class="card card--front" aria-label="Card front">
  <div class="anniversary">
    <span class="anniversary__number">25</span>
    <span class="anniversary__label">
      <span class="anniversary__small">FOR OVER</span>
      <span class="anniversary__word">Years</span>
    </span>
  </div>

  <div class="front-body">
    <div class="brand-name">BRINDLE'S</div>
    <div class="brand-sub">PAINTING &amp; RESTORATION</div>
    <p class="specialty">Waterproofing &amp; Concrete Restoration<br>Specializing in Hi-Rises &amp; Commercial</p>
    <p class="credentials">General Contractor &nbsp;CGC#4820196 &nbsp;Licensed &amp; Insured</p>
    <p class="services">
      Concrete Restoration<span class="dot">•</span>Waterproffing<span class="dot">•</span>Painting<br>
      Electrostatic<span class="dot">•</span>Expansion joints<span class="dot">•</span>Caulking<br>
      Deck Coating<span class="dot">•</span>Balustrades &amp; Railing
    </p>
  </div>
</section>

<section class="card card--back" aria-label="Card back">
  <div class="person">
    <div class="person__name">Dennis Marlow II</div>
    <div class="person__role">Supervisor / owner</div>
    <div class="person__web">www.brindlerestoration.example</div>
  </div>

  <div class="brand-faint" aria-hidden="true">BRINDLE'S<br>PAINTING &amp; RESTORATION</div>

  <div class="contact">
    <p class="contact__address">240 NE 31st Ave<br>Harbor Point, FL 33090</p>
    <p class="contact__row">
      <svg viewBox="0 0 16 16" aria-hidden="true"><path fill="#ec1f27" d="M3.5 1.5l2.5 0 1 3.5-1.8 1.2a8 8 0 0 0 4.6 4.6L11 9l3.5 1v2.5c0 1-1 2-2 2A11 11 0 0 1 1.5 3.5c0-1 1-2 2-2z"/></svg>
      555.786.0135
    </p>
    <p class="contact__row">
      <svg viewBox="0 0 16 16" aria-hidden="true"><rect x="4" y="1" width="8" height="14" rx="1.5" fill="none" stroke="#ec1f27" stroke-width="1.6"/><circle cx="8" cy="12.5" r=".9" fill="#ec1f27"/></svg>
      555.553.0154
    </p>
    <p class="contact__row">
      <svg viewBox="0 0 16 16" aria-hidden="true"><rect x="1" y="3" width="14" height="10" rx="1" fill="#ec1f27"/><path d="M1.5 3.8L8 9l6.5-5.2" fill="none" stroke="#fff" stroke-width="1.3"/></svg>
      brindlerestoration@mailcove.example
    </p>
  </div>
</section>

</body>
</html>
```